Company letter head and business card for new Indian Pharmaceutical Export company.

We need a letterhead and business card design for an Indian Pharmaceutical Export company.

The letter head needs to contain the following information.
Vorin Healthline Pvt. Ltd.
Office No 4827 Plot No 19, Larkspire, KT Lane, 400153, Maharashtra, India.
Email: info@vorin-healthline.com
Phone: +91-8342196507
CIN: U71853MH2025PTC902617
GSTIN: (This number is still pending, we will add later)

The business card needs to contain:
Address:
Vorin Healthline Pvt. Ltd.
Office No 4827 Plot No19, Larkspire, KT Lane, 400153, MH, India.
Email: torvald@vorin-healthline.com
Phone: +49-17634902851
Name on card: Torvald Ramming
Position: Director

The design for the letter head and business card should be simple but trustworthy.
Please use only Green and blue, same as in the attached logo.

```html
<!DOCTYPE html>
<html lang="en">
<head>
<meta charset="utf-8">
<title>Vorin Healthline Letterhead</title>
<link href="https://fonts.googleapis.com/css2?family=Arimo:wght@400;700&family=Open+Sans:wght@400;600&display=swap" rel="stylesheet">
<style>
  :root {
    --brand-blue: #0f5fa6;
    --brand-green: #8cc63f;
    --ink: #2b2b33;
    --ink-soft: #55555f;
    --paper: #ffffff;
    --backdrop: #e9ecef;
  }
  * { margin: 0; padding: 0; box-sizing: border-box; }
  html, body {
    width: 1200px; height: 1200px; overflow: hidden;
    background: var(--backdrop);
  }
  .letterhead {
    position: absolute; left: 204px; top: 40px;
    width: 792px; height: 1120px;
    background: var(--paper);
    box-shadow: 0 6px 24px rgba(0,0,0,.12);
    font-family: "Open Sans", Arial, sans-serif;
    color: var(--ink);
    overflow: hidden;
  }
  .brand {
    position: absolute; left: 56px; top: 52px;
    display: flex; align-items: center; gap: 10px;
  }
  .brand-dot { width: 34px; height: 34px; border-radius: 50%; background: var(--brand-blue); }
  .brand-name {
    font-family: "Arimo", Arial, sans-serif; font-weight: 700;
    font-size: 22px; color: var(--brand-blue); line-height: 1.1;
  }
  .company-address {
    position: absolute; left: 56px; top: 104px; width: 330px;
    font-family: "Arimo", Arial, sans-serif; font-size: 11.5px; line-height: 1.5;
    font-style: normal; color: #111;
  }
  .header-rule {
    position: absolute; left: 430px; top: 48px;
    width: 2px; height: 100px; background: var(--brand-blue);
  }
  .contact-list {
    position: absolute; left: 448px; top: 48px;
    font-family: "Arimo", Arial, sans-serif; font-size: 11.5px; line-height: 1.55;
    color: #111; list-style: none;
  }
  .contact-list li { display: flex; align-items: center; gap: 7px; }
  .contact-list svg { width: 11px; height: 11px; fill: var(--brand-blue); }
  .registry {
    position: absolute; left: 448px; top: 118px;
    font-family: "Arimo", Arial, sans-serif; font-size: 11.5px; line-height: 1.55; color: #111;
  }
  .registry .label { color: var(--brand-blue); }
  .letter-content {
    position: absolute; left: 100px; top: 228px; width: 600px;
  }
  .recipient {
    font-size: 12px; line-height: 1.5; color: var(--ink-soft);
    margin-bottom: 46px;
  }
  .recipient .recipient-name { font-size: 15px; color: var(--ink); letter-spacing: .3px; }
  .letter-body {
    font-size: 12.5px; line-height: 1.75; color: var(--ink);
  }
  .letter-body p { margin-bottom: 22px; text-align: justify; }
  .closing {
    margin-top: 70px;
    font-size: 13px; color: var(--ink-soft); line-height: 1.6;
  }
  .closing .signer { margin-top: 34px; font-size: 15px; color: var(--ink); }
  .footer-band {
    position: absolute; left: 0; bottom: 0; width: 100%; height: 16px;
    display: flex; gap: 6px;
  }
  .footer-band .band-blue { flex: 0 0 80%; background: var(--brand-blue); }
  .footer-band .band-green { flex: 1; background: var(--brand-green); }
</style>
</head>
<body>
  <main class="letterhead">
    <header>
      <div class="brand">
        <span class="brand-dot"></span>
        <span class="brand-name">Vorin Healthline</span>
      </div>
      <address class="company-address">
        Vorin Healthline Pvt. Ltd.<br>
        Office No 4827 Plot No 19, Larkspire,<br>
        KT Lane, 400153, Maharashtra, India.
      </address>
      <div class="header-rule"></div>
      <ul class="contact-list">
        <li><svg viewBox="0 0 24 24"><path d="M6.6 10.8a15 15 0 0 0 6.6 6.6l2.2-2.2a1 1 0 0 1 1-.25 11.4 11.4 0 0 0 3.6.57 1 1 0 0 1 1 1V20a1 1 0 0 1-1 1A17 17 0 0 1 3 4a1 1 0 0 1 1-1h3.5a1 1 0 0 1 1 1c0 1.25.2 2.450.57 3.57a1 1 0 0 1-.25 1z"/></svg>+91-8342196507</li>
        <li><svg viewBox="0 0 24 24"><path d="M2 5h20v14H2z M2 5l10 8 10-8" stroke="#fff" stroke-width="1.5"/></svg>info@vorin-healthline.com</li>
        <li><svg viewBox="0 0 24 24"><circle cx="12" cy="12" r="10"/><path d="M2 12h20M12 2c3 3 3 17 0 20M12 2c-3 3-3 17 0 20" stroke="#fff" stroke-width="1.4" fill="none"/></svg>www.vorin-healthline.com</li>
      </ul>
      <div class="registry">
        <div><span class="label">CIN:</span> U71853MH2025PTC902617</div>
        <div><span class="label">GSTIN:</span> (123456789)</div>
      </div>
    </header>

    <div class="letter-content">
      <section class="recipient">
        <div class="recipient-name">ANIKA VERHOEVEN</div>
        <div>Chief Exective Officer</div>
        <div>City/State, Zip Code</div>
      </section>

      <section class="letter-body">
        <p>Proin gravida nibh vel velit auctor aliquet. Aenean sollicitudin, lorem quis bibendum auctor, nisi elit consequat ipsum, nec sagittis sem nibh id elit. Duis sed odio sit amet nibh vulputate cursus a sit amet mauris. Morbi accumsan ipsum velit. Nam nec tellus a odio tincidunt auctor a ornare odio. Sed non mauris vitae erat consequat auctor eu in elit. Class aptent taciti sociosqu ad litora torquent ugue. Sed non neque elit. Sed ut imperdiet nisi. Proin condimentum fermentum nunc. Etiam pharetra, imperdiet nisi. Proin condimentum fermentum nunc. Etiam pharetra, erat sed fermentum feugiat, velit mauris egestas quam, ut aliquam massa nisl quis neque. Suspendisse in orci enim.</p>
        <p>This is Draftwell's version of Lorem Ipsum. Proin gravida nibh vel velit auctor aliquet. Aenean sollicitudin, lorem quis bibendum auctor, nisi elit consequat ipsum, nec sagittis sem nibh id elit. Duis sed odio sit amet nibh vulputate cursus a sit amet mauris. Mo rbi accumsan ipsum velit. Nam nec tellus a odio tincidunt auctor a ornare odio. Sed non mauris vitae erat consequat auctor eu in elit. Class aptt consequat auctor eu in elit. Class aptent taciti sociosqu ad litora torquent per conubia nostra, per inceptos himenaeos. Mauris in erat justo.</p>
        <p>Nullam ac urna eu felis dapibus condimentum sit amet a augue. Sed non neque elit. Sed ut imperdiet nisi. Proin condimentum fermentum nunc. Etiam pharetra, erat sed fermentum feugiat, velit mauris egestas quam. Nullam ac urna eu felis dapibus condimentum sit amet a aug pharetra, erat sed fermentum feugiat, velit mauris egestas quam. Nullam ac urna eu felis dapibus condimentum sit amet a augue. Sed non neque elit. Sed ut imperdiet nisi. Proin condimentum fermentum nunc.</p>
      </section>

      <section class="closing">
        <div>Sincerely,</div>
        <div class="signer">Rohan Desai</div>
      </section>
    </div>

    <footer class="footer-band">
      <span class="band-blue"></span>
      <span class="band-green"></span>
    </footer>
  </main>
</body>
</html>
```